Mesa Journey Bargains Website looking for new design

We are a online travel discounter based around hotel accommodations in Las Vegas. We need a wordpress design that will be used as our corporate cover page, and also for the affiliate pages. The current design can be viewed at http://postingloom.example/clients/mesabargain/ and the final design needs to include most of the navigation components. The affiliate pages will need a space to display the booking engine, for example, as shown at http://www.qrb-voyage.example/lorenpik. Our general color scheme is red/black, and the two logos we use are attached.

Because this is a crowded niche it is extremely important that we set ourselves apart in the design. The more visually stunning and out of the box the design, the better. The site needs to look distinctively different than anything else online. Since the overall layout is very basic and does not have to provide a lot of information, it leaves a lot of flexibility in design concepts.

We realize it is a truncated timetable, which is why the increased fee for your time and guaranteed payout.

Industry/Entity Type

Travel

```html
<!DOCTYPE html>
<html lang="en">
<head>
<meta charset="utf-8">
<title>Mesa Journey Bargains</title>
<link href="https://fonts.googleapis.com/css2?family=Open+Sans:wght@300;400;600;700&family=Arimo:wght@400;700&display=swap" rel="stylesheet">
<style>
:root{
  --red:#c40000;
  --red-bright:#e01a1a;
  --ink:#1d1d1d;
  --bar:#1e1e1e;
  --dark:#2a2a2a;
  --footer:#0b0b0b;
  --paper:#f0f0f0;
  --white:#ffffff;
  --text:#555555;
  --muted:#8a8a8a;
  --line:#dcdcdc;
  --label:#1f5a8c;
  --field:#4aa3c9;
}
*{box-sizing:border-box;margin:0;padding:0}
html,body{width:1200px;height:2498px;overflow:hidden}
body{position:relative;background:var(--white);font-family:"Arimo",Arial,sans-serif;color:var(--text)}
section,header,footer{position:absolute;left:0;width:1200px}
svg{display:block}

/* top bar */
.topbar{top:0;height:38px;background:var(--bar);color:#ddd;font-size:12px}
.topbar .item{position:absolute;top:12px;display:flex;align-items:center;gap:6px;white-space:nowrap}
.social{position:absolute;top:6px;left:1011px;display:flex;gap:4px}
.social span{width:24px;height:24px;border-radius:50%;border:2px solid var(--red);background:#2a0b0b}

/* header */
.masthead{top:38px;height:102px;background:linear-gradient(#fafafa,#eeeeee)}
.brand{position:absolute;left:44px;top:74px;display:flex;align-items:center;gap:8px}
.brand-dot{width:14px;height:14px;background:var(--red);border-radius:50%}
.brand-name{font-family:"Open Sans",sans-serif;font-weight:600;font-size:17px;color:var(--red)}
.tagline{position:absolute;left:186px;top:64px;width:290px;text-align:center;font-size:14px;color:#222;line-height:18px}
.nav{position:absolute;left:674px;top:64px;display:flex;gap:11px;font-family:"Open Sans",sans-serif;font-size:15px;color:#333}
.nav .on{color:var(--red);border-bottom:2px solid var(--red);padding-bottom:3px}

/* hero */
.hero{top:140px;height:378px;background:#eee}
.hero-photo{position:absolute;left:231px;top:0;width:969px;height:378px;background:linear-gradient(100deg,#cfc6b8 0%,#efe9df 35%,#d9cbb4 60%,#5fc9c4 82%,#9fd9e2 100%)}
.search-box{position:absolute;left:3px;top:45px;width:225px;height:324px;background:var(--white);font-size:10px;color:var(--label);padding:6px 9px}
.search-box .lbl{font-weight:700;font-size:10px;margin-top:8px;display:block}
.search-box .fld{height:25px;border:1px solid var(--field);border-radius:2px;margin-top:3px;color:#999;font-size:10px;padding:6px 5px;background:#fff}
.rooms{background:#e6f1f7;margin-top:8px;padding:5px 8px;height:70px;width:195px}
.search-btn{position:absolute;right:9px;bottom:14px;width:76px;height:26px;background:#e41b1b;color:#fff;font-weight:700;font-size:11px;border-radius:3px;text-align:center;line-height:26px}

/* features */
.features{top:518px;height:257px;background:var(--red);color:var(--white)}
.feature{position:absolute;top:0;width:388px;height:257px;text-align:center}
.feature svg{margin:48px auto 0}
.feature h3{font-family:"Open Sans",sans-serif;font-weight:400;font-size:22px;margin-top:22px}
.feature p{font-size:12px;font-weight:700;line-height:21px;margin:14px auto 0;width:330px}
.divider{position:absolute;top:38px;width:1px;height:180px;background:rgba(255,255,255,.45)}

/* about & packages */
.about{top:775px;height:576px;background:var(--paper)}
.about h2{position:absolute;left:38px;top:36px;width:210px;text-align:center;font-family:"Open Sans",sans-serif;font-weight:300;font-size:35px;color:#333}
.about .brand{left:60px;top:150px}
.about p{position:absolute;left:38px;top:252px;width:188px;font-size:12px;line-height:19px;color:var(--muted);text-align:justify}
.about p b{color:#222;font-weight:400}
.packages-title{position:absolute;left:329px;top:36px;width:831px;text-align:center;font-family:"Open Sans",sans-serif;font-size:22px;color:#333}
.packages{position:absolute;left:329px;top:73px;width:831px;height:463px;background:#fff;border:1px solid var(--line)}
.tabs{display:flex;height:40px;border-bottom:1px solid var(--line);padding-left:14px;font-size:14px;color:#444;align-items:center}
.tabs span{padding:0 14px;border-right:1px solid var(--line);line-height:16px}
.tabs span:first-child{padding-left:0}
.tabs span:last-child{border:0}
.tabs .on{color:#111}
.pkg-photos{position:absolute;left:74px;top:66px;display:flex}
.pkg-photos div{height:145px}
.pkg-text{position:absolute;left:20px;top:226px;font-size:13px;line-height:20.5px;color:var(--muted)}
.book-btn{position:absolute;left:437px;top:415px;width:83px;height:32px;background:#111;color:#fff;font-size:12px;border-radius:4px;text-align:center;line-height:32px}

/* hotel strip */
.strip{top:1351px;height:320px;background:var(--dark);color:#fff;text-align:center}
.strip h2{position:absolute;top:36px;width:100%;font-family:"Open Sans",sans-serif;font-weight:300;font-size:35px}
.strip p{position:absolute;top:106px;width:100%;font-size:13px;font-weight:700}
.hotel-row{position:absolute;left:38px;top:133px;display:flex}
.hotel-row div{width:187px;height:141px}
.next{position:absolute;left:1128px;top:190px}

/* group band */
.group{top:1671px;height:120px;background:var(--red);color:#fff;text-align:center;font-family:"Open Sans",sans-serif;font-size:35px;font-weight:400;line-height:120px}

/* contact */
.contact{top:1791px;height:383px;background:var(--paper)}
.contact h3{position:absolute;top:14px;font-family:"Open Sans",sans-serif;font-weight:400;font-size:22px;color:#222}
.agent-photo{position:absolute;left:78px;top:48px;width:124px;height:290px;border-radius:62px 62px 10px 10px;background:linear-gradient(#6a4a3a,#1d2030 55%,#151825)}
.agent-info{position:absolute;left:210px;top:130px;width:176px;text-align:right;font-size:11.5px;font-weight:700;line-height:17px;color:#111;white-space:nowrap}
.form{position:absolute;left:425px;top:50px;width:350px}
.input{height:37px;background:#fff;border:1px solid #e2e2e2;font-size:13px;color:#666;padding:11px 10px;display:flex;justify-content:space-between}
.input.msg{height:80px;margin-top:20px}
.send-btn{position:absolute;left:425px;top:285px;width:106px;height:32px;background:#111;color:#fff;border-radius:4px;font-size:13px;text-align:center;line-height:32px}
.clear{position:absolute;left:730px;top:293px;font-size:12px;color:#333}
.testimonial{position:absolute;left:814px;top:48px;width:346px;height:283px;background:#fff;border:1px solid #e2e2e2}
.testimonial p{margin:24px 22px 0;text-align:center;font-size:13px;line-height:20.5px;color:#333}
.testimonial .who{position:absolute;left:19px;top:210px;display:flex;align-items:center;gap:18px;font-size:13px;color:#333}
.avatar{width:48px;height:48px;border-radius:50%;background:linear-gradient(#5b3a30,#2f6b3a)}
.dots{position:absolute;left:970px;top:350px;display:flex;gap:5px}
.dots span{width:4px;height:4px;border-radius:50%;background:#888}

/* footer */
.footer{top:2211px;height:287px;background:var(--footer)}
.footer h4{position:absolute;top:52px;font-family:"Open Sans",sans-serif;font-weight:400;font-size:15px;color:#444;text-transform:uppercase}
.footer ul{position:absolute;top:98px;list-style:none;font-size:13px;line-height:21.5px;color:#4a4a4a}
.gallery{position:absolute;left:619px;top:98px;display:grid;grid-template-columns:repeat(4,60px);gap:3px}
.gallery div{height:58px}
.news-ring{position:absolute;left:905px;top:86px;width:60px;height:60px;border:1px solid #555;border-radius:50%}
.news{position:absolute;left:986px;top:107px;font-size:13px;color:#555;line-height:21px}
.news small{font-size:11px;display:block;line-height:14px}
.to-top{position:absolute;left:1163px;top:242px}
</style>
</head>
<body>

<header class="topbar">
  <div class="item" style="left:38px"><svg width="9" height="12" viewBox="0 0 9 12"><path d="M4.5 0a4.5 4.5 0 0 1 4.5 4.5C9 8 4.5 12 4.5 12S0 8 0 4.5A4.5 4.5 0 0 1 4.5 0z" fill="#ddd"/><circle cx="4.5" cy="4.5" r="1.6" fill="#1e1e1e"/></svg>418 Quarry Lane, Suite 12 Mesa City, NV 89990 U S A</div>
  <div class="item" style="left:418px"><svg width="8" height="12" viewBox="0 0 8 12"><rect x="1" y="0" width="6" height="12" rx="1.5" fill="#ddd"/></svg>+1-555-014-2277</div>
  <div class="item" style="left:538px"><svg width="12" height="9" viewBox="0 0 12 9"><rect width="12" height="9" fill="#ddd"/><path d="M0 0l6 5 6-5" stroke="#1e1e1e" fill="none"/></svg>info@mesabargain.travel</div>
  <div class="item" style="left:700px"><svg width="12" height="12" viewBox="0 0 12 12"><circle cx="6" cy="6" r="5" stroke="#ddd" stroke-width="1.6" fill="none"/><path d="M6 3v3h2.5" stroke="#ddd" fill="none"/></svg>24 / 7</div>
  <div class="item" style="left:782px">My Account</div>
  <div class="item" style="left:934px"><svg width="13" height="11" viewBox="0 0 13 11"><path d="M0 1h2.5l2 6h7l1.5-5H4" fill="#ddd"/><circle cx="5" cy="9.5" r="1.3" fill="#ddd"/><circle cx="10.5" cy="9.5" r="1.3" fill="#ddd"/></svg>My cart</div>
  <div class="social"><span></span><span></span><span></span><span></span><span></span><span></span></div>
</header>

<header class="masthead">
  <div class="brand"><span class="brand-dot"></span><span class="brand-name">mesabargains.travel</span></div>
  <div class="tagline">Find the best deals from thousands of hotels.<br>Guaranteed</div>
  <nav class="nav"><span class="on">HOME</span><span>GROUPS</span><span>SEARCH EVENTS</span><span>HOTELS &amp; RESORTS</span><span>CONTACT US</span></nav>
</header>

<section class="hero">
  <div class="hero-photo" role="img" aria-label="Bright hotel suite with a white bed and an open view of a turquoise sea"></div>
  <form class="search-box">
    <div style="font-size:10px">Hotel Search</div>
    <span class="lbl">Location</span>
    <div class="fld">Please type city name</div>
    <div style="display:flex;gap:6px">
      <div style="flex:1"><span class="lbl">Check-In</span><div class="fld" style="color:#222">02/20/2015</div></div>
      <div style="flex:1"><span class="lbl">Check-Out</span><div class="fld" style="color:#222">02/23/2015</div></div>
    </div>
    <div class="rooms"><b>Rooms</b>
      <div style="display:flex;gap:8px;margin-top:2px;color:#333;font-size:9px"><div>Adults<div class="fld" style="width:54px;height:20px;padding:3px;color:#222">2</div></div><div>Children<div class="fld" style="width:54px;height:20px;padding:3px;color:#222">0</div></div></div>
    </div>
    <div style="margin-top:4px;text-decoration:underline">Add another room +</div>
    <span class="lbl">Resident</span>
    <div class="fld" style="color:#222">India</div>
    <div style="margin-top:14px">Advanced options ›</div>
    <div class="search-btn">Search</div>
  </form>
</section>

<section class="features">
  <div class="feature" style="left:20px">
    <svg width="52" height="52" viewBox="0 0 52 52"><circle cx="21" cy="21" r="15" stroke="#111" stroke-width="7" fill="none"/><path d="M32 32l15 15" stroke="#111" stroke-width="9" stroke-linecap="round"/></svg>
    <h3>We find more hotels</h3>
    <p>simply dummy text of the printing and typesetting industry. Lorem Ipsum has been the industry's standard dummy text ever since the 1500s,</p>
  </div>
  <div class="divider" style="left:406px"></div>
  <div class="feature" style="left:406px">
    <svg width="52" height="52" viewBox="0 0 52 52"><path d="M4 28l13 13L48 10" stroke="#111" stroke-width="9" fill="none"/></svg>
    <h3>Best price guaranteed</h3>
    <p>100% free, no booking fees. We'll find you the best deal possible for your hotel.</p>
  </div>
  <div class="divider" style="left:794px"></div>
  <div class="feature" style="left:794px">
    <svg width="60" height="52" viewBox="0 0 60 52"><path d="M30 48C8 32 3 22 3 15 3 8 9 3 16 3c6 0 11 4 14 9 3-5 8-9 14-9 7 0 13 5 13 12 0 7-5 17-27 33z" stroke="#111" stroke-width="4" fill="none"/></svg>
    <h3>Travellers love us</h3>
    <p>simply dummy text of the printing and typesetting industry. Lorem Ipsum has been the industry's standard dummy text ever since the 1500s,</p>
  </div>
</section>

<section class="about">
  <h2>About Us</h2>
  <div class="brand"><span class="brand-dot"></span><span class="brand-name">mesabargains.travel</span></div>
  <p>MesaBargains.Travel is a Global Hotel Provider based in Las Vegas, NV.We provide hotel accommodations at wholesale pricess, for any size group, large or small... <b>read more ›</b></p>
  <div class="packages-title">Find the best packages for you</div>
  <div class="packages">
    <div class="tabs"><span>Deal of the Day</span><span>Most Popular</span><span class="on">Super Saver</span><span>Trending Now</span><span>Tab</span></div>
    <div class="pkg-photos">
      <div style="width:210px;background:linear-gradient(#0d0d18,#6b4a2a 60%,#c7833a)" role="img" aria-label="Resort tower lit at night"></div>
      <div style="width:232px;background:linear-gradient(#8a1a22,#e8e2dc 60%,#c02a2a)" role="img" aria-label="Hotel room with two beds and red headboards"></div>
      <div style="width:242px;background:linear-gradient(#6d1d22,#d7cfc6 55%,#3b2a24)" role="img" aria-label="Hotel room with a red accent wall and seating"></div>
    </div>
    <div class="pkg-text">
      Lumière Resort<br>
      Includes tour specials<br>
      Book an air + hotel package marked with the Includes tour specials offer at Lumière Resort between now and March 31, 2015<br>
      for stay dates between and and get a 2-for-1 tour special on one of the following tours:<br>
      Vegas Helicopter Strip Tour<br>
      <br>
      Hoover Dam Bus Tour<br>
      Grand Canyon Airplane Tour<br>
      Get buy one, get one 50% off on the following tour:<br>
      Grand Canyon Helicopter tour<br>
      To get this deal, be sure to the book the Includes tour specials offer
    </div>
    <div class="book-btn">Book Now</div>
  </div>
</section>

<section class="strip">
  <h2>Why not get a great hotel deal in one of these in Las Vegas?</h2>
  <p>Our price guarantee ensures you get the cheapest price online on hotels around Las Vegas</p>
  <div class="hotel-row">
    <div style="background:linear-gradient(#3a6fb0,#c79a5a 55%,#2f5a2a)" role="img" aria-label="Curved bronze hotel tower"></div>
    <div style="background:linear-gradient(#3d7fd0,#d9b07a 55%,#8a6a4a)" role="img" aria-label="Hotel facade in the afternoon"></div>
    <div style="background:linear-gradient(#4a8fd8,#c8a060 50%,#3a8fb8)" role="img" aria-label="Golden hotel tower by a pool"></div>
    <div style="background:linear-gradient(#5a9fe0,#2a5aa0 50%,#1a3a70)" role="img" aria-label="Glass pyramid hotel with palm trees"></div>
    <div style="background:linear-gradient(#1a2a6a,#c0803a 55%,#5a3a2a)" role="img" aria-label="Resort with tower and balloon sign at dusk"></div>
    <div style="background:linear-gradient(#1a2a4a,#3a4a6a 55%,#8a5a3a)" role="img" aria-label="Tall hotel towers at dusk"></div>
  </div>
  <svg class="next" width="14" height="24" viewBox="0 0 14 24"><path d="M2 2l10 10L2 22" stroke="#fff" stroke-width="3" fill="none"/></svg>
</section>

<section class="group">Need more than one room? Contact us to save on group reservations.</section>

<section class="contact">
  <h3 style="left:38px">Contact Us Today</h3>
  <div class="agent-photo" role="img" aria-label="Smiling booking agent with crossed arms"></div>
  <div class="agent-info">Name: Dana R. Whitlow<br>Email: dana.w@mailsample.example<br>Phone: 555-013-4490</div>

  <h3 style="left:540px">Need Help ?</h3>
  <div class="form">
    <div class="input"><span>Name *</span><span style="color:#ccc">●</span></div>
    <div class="input"><span>E-mail *</span><span style="color:#ccc">✉</span></div>
    <div class="input"><span>Telephone</span><span style="color:#ccc">✆</span></div>
    <div class="input msg"><span>Message *</span></div>
  </div>
  <div class="send-btn">Send message</div>
  <div class="clear">clear ⊗</div>

  <h3 style="left:924px">Testimonials</h3>
  <div class="testimonial">
    <p>Lorem Ipsum is simply dummy text of the printing and typesetting industry. Lorem Ipsum has been the industry's standard dummy text ever since the 1500s, when an unknown printer took a galley of type and scrambled it to make a type specimen book. It has survived not only five centuries, but also the leap into electronic typesetting, remaining essentially unchanged.</p>
    <div class="who"><span class="avatar" role="img" aria-label="Guest portrait"></span>Anvika – UAE</div>
  </div>
  <div class="dots"><span></span><span></span><span></span></div>
</section>

<footer class="footer">
  <h4 style="left:38px">Customer Center</h4>
  <ul style="left:38px"><li>Terms &amp; Conditions</li><li>Booking &amp; Cancellation</li><li>Customer Support</li><li>Status Enquiry</li><li>Hotels and Resorts</li></ul>
  <h4 style="left:329px">Best Deals</h4>
  <ul style="left:329px"><li>Top Deals</li><li>Popular Packages</li><li>Best Resorts</li><li>Booking Enquiry</li><li>Hot Deals</li><li>Deal Of the Day</li></ul>
  <h4 style="left:619px">Image Gallery</h4>
  <div class="gallery">
    <div style="background:linear-gradient(#3a5aa0,#b07a3a)" role="img" aria-label="Hotel at dusk"></div>
    <div style="background:linear-gradient(#7a2a8a,#d04a9a)" role="img" aria-label="Neon lit street"></div>
    <div style="background:linear-gradient(#2a3a8a,#c0a03a)" role="img" aria-label="Casino entrance"></div>
    <div style="background:linear-gradient(#1a1a3a,#a05a2a)" role="img" aria-label="Resort lights"></div>
    <div style="background:linear-gradient(#2a3a6a,#d0803a)" role="img" aria-label="Boulevard at night"></div>
    <div style="background:linear-gradient(#5a2a8a,#3a7ac0)" role="img" aria-label="Lit fountain"></div>
    <div style="background:linear-gradient(#1a2a5a,#5a6a9a)" role="img" aria-label="Glass tower"></div>
    <div style="background:linear-gradient(#4a2a2a,#c05a3a)" role="img" aria-label="Hotel towers"></div>
  </div>
  <h4 style="left:905px">News &amp; Events</h4>
  <div class="news-ring"></div>
  <div class="news">Hello world!<small>February 7, 2015</small></div>
  <svg class="to-top" width="16" height="10" viewBox="0 0 16 10"><path d="M2 8l6-6 6 6" stroke="#fff" stroke-width="2" fill="none"/></svg>
</footer>

</body>
</html>
```